Halvern Assay Advisors.

Molecular Technology Consulting. Feasibility, Evaluation and Validation of ISH/IHC and Imaging Applications.

Industry/Entity Type

Consulting

Contact Information for Business Card

Halvern Assay Advisors
Cell: 614 905-7738
Dale Morrow
dmorrow4817@quillpost.net

```html
<!DOCTYPE html>
<html lang="en">
<head>
<meta charset="utf-8">
<title>Halvern Assay Advisors — Business Card</title>
<link href="https://fonts.googleapis.com/css2?family=Lato:wght@400;700;900&display=swap" rel="stylesheet">
<style>
  :root {
    --page-bg: #e6e6e6;
    --card-black: #141414;
    --bokeh-deep: #0d1a10;
    --bokeh-green: #3f6b45;
    --brand-green: #2fae4a;
    --text-white: #ffffff;
  }
  * { margin: 0; padding: 0; box-sizing: border-box; }
  html, body {
    width: 1200px;
    height: 1000px;
    overflow: hidden;
    background: var(--page-bg);
    font-family: "Lato", sans-serif;
  }
  .sheet {
    width: 1200px;
    height: 1000px;
    display: flex;
    flex-direction: column;
    align-items: center;
    justify-content: center;
    gap: 40px;
  }
  .card {
    position: relative;
    width: 770px;
    height: 440px;
    background: var(--card-black);
    overflow: hidden;
    box-shadow: 0 6px 18px rgba(0,0,0,0.18);
  }
  .card-front__texture {
    position: absolute;
    inset: 0;
    background:
      radial-gradient(ellipse 45% 40% at 30% 30%, rgba(63,107,69,0.55), transparent 70%),
      radial-gradient(ellipse 40% 35% at 75% 55%, rgba(63,107,69,0.45), transparent 70%),
      radial-gradient(ellipse 35% 30% at 20% 80%, rgba(63,107,69,0.3), transparent 70%),
      linear-gradient(135deg, var(--bokeh-deep), var(--card-black));
  }
  .card-front__title {
    position: absolute;
    inset: 0;
    display: flex;
    flex-direction: column;
    align-items: center;
    justify-content: center;
    color: var(--text-white);
    font-weight: 900;
    font-size: 38px;
    letter-spacing: 3px;
    text-transform: uppercase;
    line-height: 1.35;
    text-align: center;
  }
  .card-back {
    display: flex;
    flex-direction: column;
    align-items: center;
    text-align: center;
  }
  .card-back__company {
    margin-top: 60px;
    color: var(--brand-green);
    font-weight: 700;
    font-size: 34px;
    letter-spacing: 4px;
    text-transform: uppercase;
    line-height: 1.3;
  }
  .card-back__name {
    margin-top: 62px;
    color: var(--text-white);
    font-weight: 400;
    font-size: 28px;
    letter-spacing: 2px;
    text-transform: uppercase;
  }
  .card-back__contact {
    margin-top: 46px;
    color: var(--text-white);
    font-size: 24px;
    letter-spacing: 1px;
    line-height: 1.5;
    list-style: none;
  }
  .card-back__label { color: var(--brand-green); }
</style>
</head>
<body>
  <main class="sheet">
    <section class="card card-front">
      <div class="card-front__texture" role="img" aria-label="Dark background with soft green bokeh light dots"></div>
      <h1 class="card-front__title">
        <span>Halvern Assay</span>
        <span>Advisors</span>
      </h1>
    </section>

    <section class="card card-back">
      <h2 class="card-back__company">Halvern Assay<br>Advisors</h2>
      <p class="card-back__name">Dale Morrow</p>
      <ul class="card-back__contact">
        <li><span class="card-back__label">M:</span> 614 905-7738</li>
        <li><span class="card-back__label">E:</span> dmorrow4817@quillpost.net</li>
      </ul>
    </section>
  </main>
</body>
</html>
```